Bref créative
Business cards, invoice, letterhead
Stationery for baby immunisation service
Professional
Thandeka Zulani
Dr
42 9th Avenue
Brenthill
Johannesburg
drtzulani@kovahealth.co.za
PR 0738261

```html
<!DOCTYPE html>
<html lang="en">
<head>
<meta charset="utf-8">
<title>Tiny Sprouts – Business Card</title>
<link href="https://fonts.googleapis.com/css2?family=Quicksand:wght@500;700&family=Open+Sans:wght@400;600&display=swap" rel="stylesheet">
<style>
  :root{
    --bg:#e9e7e3;
    --card:#ffffff;
    --green:#7dbb3f;
    --green-dark:#5e9a2a;
    --teal:#1f9bb0;
    --pink:#e0547a;
    --grey:#6f6f6f;
    --white:#ffffff;
  }
  *{box-sizing:border-box;margin:0;padding:0}
  html,body{width:1200px;height:629px;overflow:hidden;background:var(--bg)}
  .canvas{position:relative;width:1200px;height:629px}
  .card{
    position:absolute;top:171px;width:500px;height:286px;background:var(--card);
    box-shadow:0 6px 18px rgba(0,0,0,.12);overflow:hidden;
  }
  .card--front{left:70px}
  .card--back{left:630px}
  .brand{display:flex;flex-direction:column;align-items:center}
  .brand__row{display:flex;align-items:center;gap:8px}
  .brand__dot{width:14px;height:14px;border-radius:50%;background:var(--pink)}
  .brand__name{font-family:"Quicksand",sans-serif;font-weight:700;color:var(--green);}
  .brand__tagline{font-family:"Open Sans",sans-serif;color:var(--grey);font-style:italic}
  .card--front .brand{position:absolute;left:0;right:0;top:108px}
  .card--front .brand__name{font-size:40px}
  .card--front .brand__tagline{font-size:12px;margin-top:6px}
  .card--back .brand{position:absolute;left:80px;top:52px}
  .card--back .brand__name{font-size:26px}
  .card--back .brand__dot{width:10px;height:10px}
  .card--back .brand__tagline{font-size:9px;margin-top:3px}
  .wave{position:absolute;left:0;top:0;width:500px;height:286px}
  .holder{
    position:absolute;left:186px;top:196px;font-family:"Open Sans",sans-serif;
    color:var(--white);font-size:9px;line-height:1.45;
  }
  .holder__name{font-weight:600;font-size:10px}
  .contacts{
    position:absolute;left:320px;top:160px;list-style:none;font-family:"Open Sans",sans-serif;
    color:var(--white);font-size:9px;
  }
  .contacts li{display:flex;align-items:center;gap:6px;height:17px}
  .contacts svg{width:12px;height:12px;flex:none}
</style>
</head>
<body>
<main class="canvas">

  <section class="card card--front" aria-label="Business card front">
    <div class="brand">
      <div class="brand__row">
        <span class="brand__dot"></span>
        <span class="brand__name">Tiny Sprouts</span>
      </div>
      <p class="brand__tagline">caring for little ones</p>
    </div>
  </section>

  <section class="card card--back" aria-label="Business card back">
    <svg class="wave" viewBox="0 0 500 286" aria-hidden="true">
      <path d="M0 175 C140 215 320 120 500 95 L500 286 L0 286 Z" fill="var(--green)"/>
      <path d="M0 165 C140 205 320 110 500 85" fill="none" stroke="var(--teal)" stroke-width="6"/>
    </svg>

    <div class="brand">
      <div class="brand__row">
        <span class="brand__dot"></span>
        <span class="brand__name">Tiny Sprouts</span>
      </div>
      <p class="brand__tagline">caring for little ones</p>
    </div>

    <div class="holder">
      <p class="holder__name">Dr Thandeka Zulani</p>
      <p>42 9th Avenue</p>
      <p>Brenthill</p>
      <p>Johannesburg</p>
      <p>PR 0738261</p>
    </div>

    <ul class="contacts">
      <li>
        <svg viewBox="0 0 12 12"><circle cx="6" cy="6" r="6" fill="var(--white)"/><rect x="4" y="2.5" width="4" height="7" rx="1" fill="var(--green)"/></svg>
        072 555 0148
      </li>
      <li>
        <svg viewBox="0 0 12 12"><circle cx="6" cy="6" r="6" fill="var(--white)"/><path d="M3.5 3 L5 3 L5.6 4.8 L4.8 5.4 Q5.6 7 7 7.4 L7.6 6.6 L9 7.2 L9 8.6 Q5 9 3.5 3 Z" fill="var(--green)"/></svg>
        011 555 0263
      </li>
      <li>
        <svg viewBox="0 0 12 12"><circle cx="6" cy="6" r="6" fill="var(--white)"/><rect x="2.8" y="3.8" width="6.4" height="4.4" fill="none" stroke="var(--green)" stroke-width="1"/><path d="M2.8 3.8 L6 6.4 L9.2 3.8" fill="none" stroke="var(--green)" stroke-width="1"/></svg>
        drtzulani@kovahealth.co.za
      </li>
      <li>
        <svg viewBox="0 0 12 12"><circle cx="6" cy="6" r="6" fill="var(--white)"/><circle cx="6" cy="6" r="3.4" fill="none" stroke="var(--green)" stroke-width="1"/><path d="M2.6 6 H9.4 M6 2.6 Q4.2 6 6 9.4 M6 2.6 Q7.8 6 6 9.4" fill="none" stroke="var(--green)" stroke-width=".8"/></svg>
        www.tinysprouts.co.za
      </li>
    </ul>
  </section>

</main>
</body>
</html>
```